Business Card Design

our business is purchasing, rehabbing and flipping homes. Design a house in the palm of a hand. This card is for a new company based in Georgia. So we buy homes that have been foreclosed, short sales,abandond, old homes and vacant homes.
We help improve the communities that we work in. We would like to see designs that use a black background with green accent and other colors that blend and don't take away from the logo and other important information.

Industry/Entity Type

Business

Contact Information for Business Card

Hollow Pine Ventures
Turning Every Key Toward Home
2867 Ledgemoor Lane
Duluth GA 30096
Office: 678-555-0142
hollowpineventuresllc.example

```html
<!DOCTYPE html>
<html lang="en">
<head>
<meta charset="utf-8">
<title>Hollow Pine Ventures – Business Card</title>
<link href="https://fonts.googleapis.com/css2?family=Cinzel:wght@600&family=Open+Sans:wght@400;600&display=swap" rel="stylesheet">
<style>
  :root {
    --backdrop: #d8d3ca;
    --card: #0c0c0c;
    --card-edge: #1c1c1c;
    --green: #9bcb3c;
    --white: #f4f4f2;
    --muted: #e2e2e0;
  }
  html, body {
    margin: 0;
    width: 1200px;
    height: 780px;
    overflow: hidden;
    background: var(--backdrop);
  }
  .card {
    position: absolute;
    left: 100px;
    top: 104px;
    width: 1000px;
    height: 572px;
    border-radius: 22px;
    background: linear-gradient(135deg, #161616 0%, var(--card) 55%, #080808 100%);
    box-shadow: 0 0 0 1px var(--card-edge), 0 18px 40px rgba(0,0,0,.35);
    color: var(--white);
    font-family: "Open Sans", Arial, sans-serif;
  }
  .brand {
    position: absolute;
    left: 40px;
    top: 120px;
    width: 400px;
    text-align: center;
  }
  .brand-mark {
    display: block;
    width: 96px;
    height: 96px;
    margin: 0 auto 34px;
    background: var(--green);
    border-radius: 6px;
  }
  .brand-name {
    display: flex;
    align-items: center;
    gap: 16px;
    font-family: "Cinzel", Georgia, serif;
    font-weight: 600;
    font-size: 31px;
    letter-spacing: 1px;
    color: var(--white);
    white-space: nowrap;
  }
  .brand-name::before,
  .brand-name::after {
    content: "";
    flex: 1;
    height: 2px;
    background: var(--green);
  }
  .brand-tagline {
    margin-top: 10px;
    font-family: "Cinzel", Georgia, serif;
    font-size: 19px;
    color: var(--green);
  }
  .divider {
    position: absolute;
    left: 470px;
    top: 60px;
    width: 2px;
    height: 452px;
    background: linear-gradient(to bottom, transparent, var(--green) 25%, var(--green) 75%, transparent);
  }
  .details {
    position: absolute;
    left: 530px;
    top: 92px;
  }
  .person-name {
    margin: 0;
    font-family: "Cinzel", Georgia, serif;
    font-weight: 600;
    font-size: 42px;
    letter-spacing: 1px;
    line-height: 1.1;
  }
  .person-role {
    margin: 4px 0 34px;
    font-size: 27px;
    color: var(--green);
  }
  .address {
    margin: 0 0 30px;
    font-size: 22px;
    line-height: 1.35;
    color: var(--muted);
  }
  .contact-list {
    list-style: none;
    margin: 0;
    padding: 0;
  }
  .contact-list li {
    display: flex;
    align-items: center;
    gap: 14px;
    font-size: 22px;
    line-height: 1.5;
    color: var(--muted);
  }
  .contact-icon {
    width: 24px;
    height: 24px;
    flex: none;
  }
</style>
</head>
<body>
  <main class="card">
    <section class="brand">
      <span class="brand-mark"></span>
      <div class="brand-name">Hollow Pine Ventures</div>
      <div class="brand-tagline">Turning Every Key Toward Home</div>
    </section>

    <div class="divider"></div>

    <section class="details">
      <h1 class="person-name">EMPLOYEE NAME</h1>
      <p class="person-role">Managing Director</p>
      <p class="address">2867 Ledgemoor Lane Duluth<br>GA 30096</p>
      <ul class="contact-list">
        <li>
          <svg class="contact-icon" viewBox="0 0 24 24" aria-hidden="true">
            <rect width="24" height="24" rx="4" fill="var(--green)"/>
            <path d="M8 6l2.5 0 1 3-1.6 1.2a8 8 0 0 0 3.9 3.9L15 12.5l3 1V16c0 1-1 2-2 2A10 10 0 0 1 6 8c0-1 1-2 2-2z" fill="#0c0c0c"/>
          </svg>
          678-555-0142
        </li>
        <li>
          <svg class="contact-icon" viewBox="0 0 24 24" aria-hidden="true">
            <rect width="24" height="24" rx="4" fill="var(--green)"/>
            <rect x="5" y="7" width="14" height="10" fill="none" stroke="#0c0c0c" stroke-width="1.8"/>
            <path d="M5 7l7 6 7-6" fill="none" stroke="#0c0c0c" stroke-width="1.8"/>
          </svg>
          your@hollowpineventures.example
        </li>
        <li>
          <svg class="contact-icon" viewBox="0 0 24 24" aria-hidden="true">
            <rect width="24" height="24" rx="4" fill="var(--green)"/>
            <circle cx="12" cy="12" r="6.5" fill="none" stroke="#0c0c0c" stroke-width="1.6"/>
            <ellipse cx="12" cy="12" rx="2.8" ry="6.5" fill="none" stroke="#0c0c0c" stroke-width="1.4"/>
            <path d="M5.5 12h13" stroke="#0c0c0c" stroke-width="1.4"/>
          </svg>
          www.hollowpineventuresllc.example
        </li>
      </ul>
    </section>
  </main>
</body>
</html>
```